8 1/2 x 8 1/2 Social Media Design Ad - Commercial Loan Originator

Wanted
Commercial Loan Originators

* No Licensing Required
* Lend Nationwide with few exceptions
* Competitive Compensation
* You find the Investors and we handle the rest!!!

PRODUCTS
* Debt Service Coverage Loans (DSCR)
* Fix & Flip Financing
* Ground Up Construction
* Bridge Loans
* Portfolio Loans
And many more.....

Call (800) 417-9265 x24 for more information

Brightmoor Lending Partners, Inc.
7200 Warbleton Avenue, Ellicott City, MD 21043
NMLS #318640

```html
<!DOCTYPE html>
<html lang="en">
<head>
<meta charset="utf-8">
<title>Brightmoor Lending Partners – Now Hiring Commercial Loan Originators</title>
<link href="https://fonts.googleapis.com/css2?family=Playfair+Display:wght@700&family=Montserrat:wght@500;600&display=swap" rel="stylesheet">
<style>
  :root {
    --navy-deep: #0b1a2c;
    --navy: #16304d;
    --sky: #5f86ad;
    --gold-light: #f6e3a8;
    --gold: #d9b96a;
    --gold-dark: #a9843a;
    --white: #ffffff;
    --ink: #14202e;
    --suit: #3a4a5e;
  }
  * { margin: 0; padding: 0; box-sizing: border-box; }
  html, body { width: 1200px; height: 1200px; overflow: hidden; background: var(--navy-deep); }
  .ad {
    position: relative;
    width: 1200px;
    height: 1200px;
    overflow: hidden;
    font-family: "Montserrat", Arial, sans-serif;
    color: var(--white);
  }
  .scene-photo {
    position: absolute; inset: 0;
    background:
      linear-gradient(180deg, #7fa3c6 0%, #4d6f93 30%, #3a4e63 55%, #202c38 78%, #151c24 100%);
  }
  .person-photo {
    position: absolute;
    left: 590px; top: 0; width: 610px; height: 1200px;
    background:
      radial-gradient(ellipse 45% 20% at 56% 22%, rgba(90,58,40,0.85), rgba(90,58,40,0) 100%),
      radial-gradient(ellipse 70% 55% at 55% 78%, rgba(58,74,94,0.95), rgba(58,74,94,0) 100%),
      linear-gradient(180deg, rgba(200,210,220,0.35), rgba(40,52,68,0.3));
  }
  .left-shade {
    position: absolute; inset: 0;
    background: linear-gradient(90deg, rgba(11,26,44,0.92) 0%, rgba(16,38,62,0.78) 38%, rgba(16,38,62,0.25) 55%, rgba(16,38,62,0) 65%);
  }
  .brand {
    position: absolute;
    left: 118px; top: 150px; width: 480px;
    display: flex; align-items: center; justify-content: center; gap: 18px;
  }
  .brand-dot {
    width: 34px; height: 34px; border-radius: 50%;
    background: var(--gold); flex: none;
  }
  .brand-name {
    font-family: "Playfair Display", Georgia, serif;
    font-weight: 700;
    font-size: 38px;
    line-height: 1.15;
    color: var(--gold);
    text-align: center;
  }
  .hiring-band {
    position: absolute;
    left: 90px; top: 415px; width: 510px; height: 48px;
    background: linear-gradient(90deg, rgba(217,185,106,0) 0%, var(--gold-light) 14%, var(--gold) 60%, rgba(217,185,106,0) 100%);
    display: flex; align-items: center; justify-content: center;
    font-weight: 600; font-size: 38px; letter-spacing: 2px;
    color: var(--ink);
    padding-right: 30px;
  }
  .headline {
    position: absolute;
    left: 40px; top: 510px; width: 640px;
    text-align: center;
    font-family: "Playfair Display", Georgia, serif;
    font-weight: 700;
    font-size: 66px;
    line-height: 86px;
    letter-spacing: -0.5px;
  }
  .rule {
    position: absolute; left: 80px; width: 570px; height: 2px;
    background: linear-gradient(90deg, rgba(217,185,106,0), var(--gold) 20%, var(--gold) 75%, rgba(217,185,106,0));
  }
  .rule-top { top: 715px; }
  .rule-bottom { top: 793px; }
  .tagline {
    position: absolute; left: 40px; top: 738px; width: 660px;
    text-align: center; font-size: 25px; font-weight: 500; letter-spacing: 0.5px;
  }
  .perks { position: absolute; left: 118px; top: 830px; list-style: none; }
  .perk {
    display: flex; align-items: center; gap: 22px;
    font-size: 28px; font-weight: 500; letter-spacing: 1px;
    height: 56px;
  }
  .perk svg { width: 28px; height: 28px; flex: none; }
  .call-button {
    position: absolute;
    left: 94px; top: 985px; width: 522px; height: 74px;
    border-radius: 8px;
    background: linear-gradient(180deg, var(--gold-light) 0%, var(--gold) 55%, var(--gold-dark) 100%);
    border: 2px solid #f3dd9c;
    display: flex; align-items: center; justify-content: center; gap: 10px;
    color: var(--ink);
    font-size: 37px; font-weight: 500;
  }
  .call-ext { font-size: 27px; }
</style>
</head>
<body>
<main class="ad">
  <div class="scene-photo" role="img" aria-label="Two-storey suburban house and quiet street under a blue cloudy sky"></div>
  <div class="person-photo" role="img" aria-label="Smiling businessman in a grey suit and white tie with arms crossed"></div>
  <div class="left-shade"></div>

  <div class="brand">
    <span class="brand-dot"></span>
    <span class="brand-name">Brightmoor Lending Partners, Inc.</span>
  </div>

  <div class="hiring-band">NOW HIRING</div>

  <h1 class="headline">Commercial Loan<br>Originators</h1>

  <div class="rule rule-top"></div>
  <p class="tagline">You find the investors. We handle the rest.</p>
  <div class="rule rule-bottom"></div>

  <ul class="perks">
    <li class="perk">
      <svg viewBox="0 0 28 28" aria-hidden="true"><circle cx="14" cy="14" r="11.5" fill="none" stroke="#d9b96a" stroke-width="2.5"/><path d="M8.5 14.5l4 4 7.5-8" fill="none" stroke="#d9b96a" stroke-width="2.5" stroke-linecap="round" stroke-linejoin="round"/></svg>
      No Licensing Required
    </li>
    <li class="perk">
      <svg viewBox="0 0 28 28" aria-hidden="true"><circle cx="14" cy="14" r="11.5" fill="none" stroke="#d9b96a" stroke-width="2.5"/><path d="M8.5 14.5l4 4 7.5-8" fill="none" stroke="#d9b96a" stroke-width="2.5" stroke-linecap="round" stroke-linejoin="round"/></svg>
      Competitive Compensation
    </li>
  </ul>

  <div class="call-button">Call (800) 417-9265 <span class="call-ext">x24</span></div>
</main>
</body>
</html>
```